Menu Board 1000mmx500mm re-design

I would like to re-design exiting menu board 1000mmx500mm. Current board letters are bit to small to read. I would like to have pictures (attached) of the food offered on it and at the same time to create balance between pictures and size of the text to be easily readable. Fonts and colours are up to designer choice but prefer warm and bright colours rather anything dark.

Target Market(s)

Food industry

Industry/Entity Type

Food

Font styles to use
Other font styles liked:
• I leave font choice to designer

Colors
FFC000
F8CF3A
FAE287
FDF2CF
FEFAEE
F0912C
F2A743
F7CA91
FBE8D2
FDF5EE
EE7325
F08F49
F5BC92
FAE3D3
FDF4ED

Requirements
Must have
• Pictures + Text
Nice to have
• Balance between images and text.
Should not have
• Can't think of any

```html
<!DOCTYPE html>
<html lang="en">
<head>
<meta charset="utf-8">
<title>Menu Board</title>
<link href="https://fonts.googleapis.com/css2?family=Oswald:wght@500&family=Roboto:wght@400&family=Permanent+Marker&display=swap" rel="stylesheet">
<style>
  :root {
    --orange: #e8531f;
    --yellow: #fdc300;
    --ink: #1e1e1e;
    --board: #f3f3f3;
    --backdrop: #bdbdbd;
    --white: #ffffff;
  }
  html, body { margin: 0; padding: 0; overflow: hidden; }
  body { width: 1200px; height: 1200px; background: var(--backdrop); position: relative; }
  .board {
    position: absolute; left: 375px; top: 114px;
    width: 730px; height: 1458px;
    transform: scale(0.625); transform-origin: 0 0;
    background: linear-gradient(180deg, #f7f7f7, #ececec);
    overflow: hidden;
    box-shadow: 0 20px 40px rgba(0,0,0,.25);
  }
  .hero {
    position: absolute; left: 0; top: 0; width: 730px; height: 300px;
    background: radial-gradient(ellipse at 55% 40%, #f7c24a, #d98a1a 55%, #8a4a12 100%);
  }
  .hero-band { position: absolute; left: 0; top: 230px; width: 730px; height: 130px; }
  .dish-circle {
    position: absolute; border-radius: 50%;
    border: 6px solid var(--orange); box-sizing: border-box;
  }
  .dish-ciabatta { left: 65px; top: 242px; width: 170px; height: 170px; background: radial-gradient(circle at 50% 45%, #c89a5a, #7a4e26 70%, #e9e9e9 72%); }
  .dish-chicken { left: 270px; top: 220px; width: 200px; height: 200px; background: radial-gradient(circle at 40% 50%, #d49a3c, #f1ead6 45%, #6e4424 75%); }
  .dish-wrap { left: 500px; top: 242px; width: 170px; height: 170px; background: radial-gradient(circle at 50% 45%, #e6cfa1, #b68a52 60%, #ececec 72%); }
  .menu-title {
    position: absolute; left: 0; width: 730px; top: 440px; text-align: center;
    font-family: "Permanent Marker", cursive; font-size: 128px; color: var(--ink);
    margin: 0; line-height: 1;
  }
  .item { position: absolute; width: 320px; height: 146px; }
  .item-name {
    font-family: "Oswald", sans-serif; font-weight: 500; color: var(--orange);
    font-size: 23px; line-height: 27px; margin: 0; text-transform: uppercase; width: 170px;
  }
  .item-desc {
    font-family: "Roboto", sans-serif; font-size: 15px; line-height: 16.5px;
    color: var(--ink); margin: 4px 0 0; width: 165px;
  }
  .price {
    position: absolute; left: 0; bottom: 0; height: 40px; min-width: 64px; padding: 0 10px;
    box-sizing: border-box; background: var(--yellow); border-radius: 3px;
    font-family: "Oswald", sans-serif; font-size: 26px; line-height: 40px; color: var(--ink);
    text-align: center;
  }
  .price small { font-size: 15px; margin-right: 2px; }
  .item-photo {
    position: absolute; right: 0; top: 0; width: 146px; height: 146px;
    border: 4px solid var(--orange); border-radius: 6px; box-sizing: border-box;
    box-shadow: inset 0 0 0 3px var(--white);
  }
  .drink {
    position: absolute; top: 1140px; width: 320px; height: 146px;
    background: var(--orange); border-radius: 4px;
  }
  .drink-photo { position: absolute; left: 8px; top: 8px; width: 130px; height: 130px; border-radius: 3px; box-shadow: 0 0 0 2px var(--white); }
  .drink-name {
    position: absolute; left: 155px; top: 30px; margin: 0;
    font-family: "Oswald", sans-serif; font-weight: 500; font-size: 28px; color: var(--white);
  }
  .drink .price { left: 155px; top: 74px; bottom: auto; }
  .sauce-band { position: absolute; left: 0; top: 1310px; width: 730px; height: 148px; }
  .sauce-label {
    position: absolute; left: 263px; top: 1315px; width: 204px; height: 66px;
    background: var(--yellow); border-radius: 6px; text-align: center;
    font-family: "Oswald", sans-serif; font-weight: 500; font-size: 46px; line-height: 66px; color: var(--ink);
  }
  .sauce-list {
    position: absolute; left: 28px; right: 28px; top: 1404px; margin: 0; padding: 0; list-style: none;
    display: flex; justify-content: space-between;
    font-family: "Oswald", sans-serif; font-weight: 500; font-size: 23px; color: var(--white);
  }
  .sauce-list li { display: flex; align-items: center; gap: 6px; }
  .tick { width: 14px; height: 14px; background: var(--yellow); border-radius: 2px; display: inline-block; position: relative; }
  .tick svg { position: absolute; left: 2px; top: 2px; }
</style>
</head>
<body>
<div class="board">
  <div class="hero" role="img" aria-label="Photo of golden roasted potatoes with thyme"></div>
  <svg class="hero-band" viewBox="0 0 730 130" aria-hidden="true">
    <path d="M0 0 L730 0 L730 80 C600 120 500 95 380 110 C250 125 130 95 0 105 Z" fill="#f3f3f3"/>
    <path d="M0 20 C120 60 240 40 370 65 C500 85 620 50 730 40 L730 60 C620 75 500 105 370 90 C240 72 120 85 0 60 Z" fill="#e8531f"/>
  </svg>
  <div class="dish-circle dish-ciabatta" role="img" aria-label="Photo of a chicken ciabatta sandwich"></div>
  <div class="dish-circle dish-chicken" role="img" aria-label="Photo of roast chicken with veggie rice"></div>
  <div class="dish-circle dish-wrap" role="img" aria-label="Photo of a grilled chicken wrap"></div>

  <h1 class="menu-title">MENU</h1>

  <div class="item" style="left:30px; top:607px;">
    <h2 class="item-name">Ciabatta</h2>
    <p class="item-desc">Roti Chicken, Rucola, Caramelized Onions, Tomato, Fresh Onion</p>
    <div class="price"><small>£</small>6</div>
    <div class="item-photo" style="background:linear-gradient(160deg,#f2f2f2,#d9b27a 55%,#a06a36);" role="img" aria-label="Photo of a grilled chicken ciabatta"></div>
  </div>
  <div class="item" style="left:380px; top:607px;">
    <h2 class="item-name">1/4 Chicken Box</h2>
    <p class="item-desc">Roti Chicken, Veggie Rice &amp; Salad</p>
    <div class="price"><small>£</small>9</div>
    <div class="item-photo" style="background:linear-gradient(135deg,#c98a3a,#efe7d2 55%,#6b4426);" role="img" aria-label="Photo of quarter roast chicken with rice"></div>
  </div>

  <div class="item" style="left:30px; top:784px;">
    <h2 class="item-name">Wrap</h2>
    <p class="item-desc">Roti Chicken, Crunchy Slaw, Tomato, Fresh Onion &amp; Sauce of your choice</p>
    <div class="price"><small>£</small>7</div>
    <div class="item-photo" style="background:linear-gradient(160deg,#4f6b34,#e3c37a 50%,#b64a2e);" role="img" aria-label="Photo of a chicken wrap cut in half"></div>
  </div>
  <div class="item" style="left:380px; top:784px;">
    <h2 class="item-name">1/2 Chicken Box</h2>
    <p class="item-desc">Roti Chicken, Veggie Rice &amp; Salad</p>
    <div class="price"><small>£</small>14</div>
    <div class="item-photo" style="background:linear-gradient(135deg,#c98a3a,#efe7d2 55%,#6b4426);" role="img" aria-label="Photo of half roast chicken with rice"></div>
  </div>

  <div class="item" style="left:30px; top:962px;">
    <h2 class="item-name">Beetroot Wrap</h2>
    <p class="item-desc">Roti Chicken, Crunchy Slaw, Tomato, Fresh Onion &amp; Sauce of your choice</p>
    <div class="price"><small>£</small>8</div>
    <div class="item-photo" style="background:linear-gradient(160deg,#8a2a3a,#d9c0a8 50%,#4e6b34);" role="img" aria-label="Photo of a beetroot chicken wrap"></div>
  </div>
  <div class="item" style="left:380px; top:962px;">
    <h2 class="item-name">Roasted Potatoes</h2>
    <p class="item-desc">Thyme &amp; Garlic</p>
    <div class="price"><small>£</small>2.5</div>
    <div class="item-photo" style="background:linear-gradient(135deg,#f2b33c,#d9761c 55%,#2f3550);" role="img" aria-label="Photo of roasted potatoes"></div>
  </div>

  <div class="drink" style="left:30px;">
    <div class="drink-photo" style="background:linear-gradient(160deg,#e8f4fb,#5aa8db);" role="img" aria-label="Photo of a bottle of water"></div>
    <h2 class="drink-name">WATER</h2>
    <div class="price"><small>£</small>1</div>
  </div>
  <div class="drink" style="left:380px;">
    <div class="drink-photo" style="background:linear-gradient(90deg,#e6e6e6,#f7a51c 50%,#e6e6e6);" role="img" aria-label="Photo of a glass of orange juice"></div>
    <h2 class="drink-name">CAN &amp; JUICES</h2>
    <div class="price"><small>£</small>1.8</div>
  </div>

  <svg class="sauce-band" viewBox="0 0 730 148" aria-hidden="true">
    <path d="M0 50 C200 10 520 0 730 70 L730 148 L0 148 Z" fill="#fdc300"/>
    <path d="M0 80 C200 35 520 30 730 85 L730 148 L0 148 Z" fill="#e8531f"/>
  </svg>
  <div class="sauce-label">SAUCES</div>
  <ul class="sauce-list">
    <li><span class="tick"><svg width="10" height="10" viewBox="0 0 10 10"><path d="M1 5 L4 8 L9 2" fill="none" stroke="#e8531f" stroke-width="2"/></svg></span>SIGNATURE</li>
    <li><span class="tick"><svg width="10" height="10" viewBox="0 0 10 10"><path d="M1 5 L4 8 L9 2" fill="none" stroke="#e8531f" stroke-width="2"/></svg></span>SWEET CHILLI</li>
    <li><span class="tick"><svg width="10" height="10" viewBox="0 0 10 10"><path d="M1 5 L4 8 L9 2" fill="none" stroke="#e8531f" stroke-width="2"/></svg></span>BBQ</li>
    <li><span class="tick"><svg width="10" height="10" viewBox="0 0 10 10"><path d="M1 5 L4 8 L9 2" fill="none" stroke="#e8531f" stroke-width="2"/></svg></span>GARLIC MAYO</li>
    <li><span class="tick"><svg width="10" height="10" viewBox="0 0 10 10"><path d="M1 5 L4 8 L9 2" fill="none" stroke="#e8531f" stroke-width="2"/></svg></span>PIRI PIRI</li>
  </ul>
</div>
</body>
</html>
```